Wendlow Cellars -responsive, bootstrap website design

Looking to build a responsive service website.

Logo and pictures have been provided.

PLEASE REVIEW ATTACHED DESIGN STYLE GUIDES & CLIENT CREATIVE BRIEF FOR OUR REQUIREMENT. THANK YOU AND GOOD LUCK!

```html
<!DOCTYPE html>
<html lang="en">
<head>
<meta charset="utf-8">
<title>Wendlow Cellars – The Wendlow Story</title>
<link rel="stylesheet" href="https://fonts.googleapis.com/css2?family=Tinos:wght@400;700&display=swap">
<style>
  :root {
    --page-bg: #0b0b0b;
    --accent: #e0861c;
    --accent-light: #f8a93a;
    --accent-dark: #b8660f;
    --text-light: #ffffff;
    --button-text: #1a1005;
    --logo-bg: #ffffff;
    --logo-ink: #1c1c1c;
  }
  * { box-sizing: border-box; margin: 0; padding: 0; }
  html, body {
    width: 1200px; height: 900px; overflow: hidden;
    background: var(--page-bg);
    font-family: "Tinos", "Times New Roman", serif;
  }
  .page { position: relative; width: 1200px; height: 900px; overflow: hidden; }

  .vineyard-photo {
    position: absolute; left: 280px; top: 180px; width: 880px; height: 560px;
    background:
      radial-gradient(ellipse 60% 40% at 55% 15%, rgba(150,150,150,.45), transparent 70%),
      radial-gradient(ellipse 70% 55% at 55% 55%, rgba(80,80,80,.55), transparent 75%);
  }
  .grapes-photo {
    position: absolute; left: 880px; top: 600px; width: 320px; height: 300px;
    background: radial-gradient(ellipse 45% 50% at 50% 50%, rgba(70,70,70,.6), transparent 75%);
  }
  .bottle-photo {
    position: absolute; left: 165px; top: 152px; width: 180px; height: 668px;
    border-radius: 40px 40px 14px 14px;
    background: linear-gradient(90deg, #14141c 0%, #2a1820 30%, #0d0a0e 60%, #1c1c24 100%);
    box-shadow: 0 0 30px rgba(255,255,255,.12);
  }

  .main-nav a {
    position: absolute; top: 75px;
    color: var(--accent); font-size: 12.5px; text-decoration: none; text-transform: uppercase;
  }

  .brand {
    position: absolute; left: 505px; top: 10px; width: 190px; height: 190px;
    border-radius: 50%; background: var(--logo-bg);
    display: flex; align-items: center; justify-content: center;
  }
  .brand-name {
    color: var(--logo-ink); font-size: 26px; font-weight: 400; text-align: center; line-height: 1.1;
  }

  .story { position: absolute; left: 372px; top: 410px; width: 735px; }
  .story-title {
    color: var(--accent); font-size: 29px; font-weight: 400; letter-spacing: 1px;
    text-transform: uppercase; margin-bottom: 22px;
  }
  .story p {
    color: var(--text-light); font-size: 16.6px; line-height: 26px; margin-bottom: 26px;
  }
  .join-button {
    display: inline-block; width: 204px; height: 36px; line-height: 36px;
    margin-top: 1px; text-align: center; border-radius: 6px;
    border: 1px solid var(--accent-light);
    background: linear-gradient(180deg, var(--accent-light) 0%, var(--accent) 60%, var(--accent-dark) 100%);
    color: var(--button-text); font-size: 12.5px; text-decoration: none; text-transform: uppercase;
  }
</style>
</head>
<body>
<div class="page">
  <div class="vineyard-photo" role="img" aria-label="Black and white photo of rolling vineyard hills under an evening sky"></div>
  <div class="grapes-photo" role="img" aria-label="Dark photo of a grape cluster hanging on the vine"></div>
  <div class="bottle-photo" role="img" aria-label="Photo of a Wendlow Cellars Cabernet Sauvignon bottle with a silver label"></div>

  <nav class="main-nav">
    <a href="#" style="left:122px">Home</a>
    <a href="#" style="left:240px">About</a>
    <a href="#" style="left:293px">Wines</a>
    <a href="#" style="left:415px">Store</a>
    <a href="#" style="left:748px">News</a>
    <a href="#" style="left:865px">Join the Wendlow Family</a>
  </nav>

  <div class="brand"><span class="brand-name">Wendlow<br>Cellars</span></div>

  <section class="story">
    <h1 class="story-title">The Wendlow Story</h1>
    <p>A love for wine has been in my family long before I was born.&nbsp; My ancestors viewed wine as simply an essential part of daily life.&nbsp; Rosaria, my great grandmother, knew each family in her small Italian neighborhood by their homemade wine.&nbsp; For her, a person’s very character was built on the quality of their craft.</p>
    <p>Now, with Wendlow Cellars, I hope to honor the tradition my family has had with wine for over a century.&nbsp; I hope that you too will become a part of Famiglia Wendlow and taste what for me is so elemental to the joy of life.</p>
    <p>Welcome to Wendlow Cellars.</p>
    <a href="#" class="join-button">Join the Wendlow Family</a>
  </section>
</div>
</body>
</html>
```